Integrated content management graphic

We are looking for a creative iteration for the attached file. We are currently in the process of renewing our branding and this graphic will be a center piece to our product marketing. Our website is www.brelvanto-docuhub.com for more information on products and company.
Future projects are available for designers submitting outstanding concepts and branding capability.

Target Market(s)

Audience is IT and anyone interested in integrating content management with their ERP/Accounting system.

Industry/Entity Type

Construction

Requirements
Must have
• The design must use the current color scheme associated with our website, yellow, black, grey. White can also be used. The design should be sleek.
Nice to have
• 3D Feel. The wheel could take on a stadium concept in 3d.

```html
<!DOCTYPE html>
<html lang="en">
<head>
<meta charset="utf-8">
<title>Integrated Content Management Wheel</title>
<link rel="stylesheet" href="https://fonts.googleapis.com/css2?family=Montserrat:wght@600;800&display=swap">
<style>
  :root {
    --bg-center: #3a3a3a;
    --bg-edge: #121212;
    --yellow: #ffe100;
    --yellow-soft: #e8d41a;
    --yellow-deep: #cdb60a;
    --yellow-mid: #c9b10c;
    --olive: #857812;
    --ink: #1c1c1c;
    --gap: #1a1a1a;
  }
  html, body {
    margin: 0;
    padding: 0;
    overflow: hidden;
    background: var(--bg-edge);
  }
  .canvas {
    width: 1200px;
    height: 1122px;
    position: relative;
    overflow: hidden;
    background: radial-gradient(ellipse at 50% 45%, var(--bg-center) 0%, #222 45%, var(--bg-edge) 100%);
    font-family: "Montserrat", sans-serif;
  }
  .wheel {
    position: absolute;
    left: 0;
    top: 0;
  }
  .label {
    font-family: "Montserrat", sans-serif;
    font-weight: 600;
    text-transform: uppercase;
  }
  .label-outer { fill: var(--yellow); font-size: 34px; letter-spacing: 1px; }
  .label-middle { fill: var(--ink); font-size: 30px; }
  .label-middle-small { fill: var(--ink); font-size: 24px; }
  .label-inner { fill: var(--ink); font-size: 27px; font-weight: 800; }
  .label-inner-small { fill: var(--ink); font-size: 21px; font-weight: 800; }
  .brand-mark {
    font-family: "Montserrat", sans-serif;
    font-weight: 800;
    fill: var(--yellow);
  }
</style>
</head>
<body>
<div class="canvas">
  <svg class="wheel" width="1200" height="1122" viewBox="0 0 1200 1122" xmlns="http://www.w3.org/2000/svg">
    <defs>
      <radialGradient id="outer-ring-fill" gradientUnits="userSpaceOnUse" cx="0" cy="0" r="460">
        <stop offset="0.78" stop-color="#5c5c5c"/>
        <stop offset="0.88" stop-color="#3e3e3e"/>
        <stop offset="1" stop-color="#2a2a2a"/>
      </radialGradient>
      <radialGradient id="bevel-fill" gradientUnits="userSpaceOnUse" cx="0" cy="0" r="372">
        <stop offset="0.9" stop-color="#bdbdbd"/>
        <stop offset="0.96" stop-color="#7a7a7a"/>
        <stop offset="1" stop-color="#3a3a3a"/>
      </radialGradient>
      <radialGradient id="inner-fill" gradientUnits="userSpaceOnUse" cx="0" cy="0" r="180">
        <stop offset="0.4" stop-color="#f0f0f0"/>
        <stop offset="1" stop-color="#a8a8a8"/>
      </radialGradient>
      <radialGradient id="hub-fill" cx="0.45" cy="0.4" r="0.6">
        <stop offset="0" stop-color="#2e2e2e"/>
        <stop offset="1" stop-color="#0c0c0c"/>
      </radialGradient>

      <path id="cw-398" d="M0,398 A398,398 0 1 1 0,-398 A398,398 0 1 1 0,398"/>
      <path id="cw-278" d="M0,278 A278,278 0 1 1 0,-278 A278,278 0 1 1 0,278"/>
      <path id="cw-262" d="M0,262 A262,262 0 1 1 0,-262 A262,262 0 1 1 0,262"/>
      <path id="cw-132" d="M0,132 A132,132 0 1 1 0,-132 A132,132 0 1 1 0,132"/>
      <path id="cw-140" d="M0,140 A140,140 0 1 1 0,-140 A140,140 0 1 1 0,140"/>
      <path id="cw-112" d="M0,112 A112,112 0 1 1 0,-112 A112,112 0 1 1 0,112"/>
      <path id="ccw-428" d="M0,-428 A428,428 0 1 0 0,428 A428,428 0 1 0 0,-428"/>
      <path id="ccw-278" d="M0,-278 A278,278 0 1 0 0,278 A278,278 0 1 0 0,-278"/>
      <path id="ccw-252" d="M0,-252 A252,252 0 1 0 0,252 A252,252 0 1 0 0,-252"/>
      <path id="ccw-150" d="M0,-150 A150,150 0 1 0 0,150 A150,150 0 1 0 0,-150"/>
    </defs>

    <g class="wheel-body" transform="translate(582,514)">
      <circle r="464" fill="var(--gap)"/>
      <circle r="460" fill="none" stroke="#555" stroke-width="2"/>

      <!-- outer business-system ring: six segments with equal 3° gaps -->
      <g class="outer-ring" fill="none" stroke="url(#outer-ring-fill)" stroke-width="86">
        <circle r="413" pathLength="360" stroke-dasharray="48 312" transform="rotate(-116)"/>
        <circle r="413" pathLength="360" stroke-dasharray="59 301" transform="rotate(-65)"/>
        <circle r="413" pathLength="360" stroke-dasharray="79 281" transform="rotate(-3)"/>
        <circle r="413" pathLength="360" stroke-dasharray="24 336" transform="rotate(79)"/>
        <circle r="413" pathLength="360" stroke-dasharray="59 301" transform="rotate(106)"/>
        <circle r="413" pathLength="360" stroke-dasharray="73 287" transform="rotate(168)"/>
      </g>

      <circle r="356" fill="none" stroke="url(#bevel-fill)" stroke-width="30"/>
      <circle r="341" fill="none" stroke="#2a2a2a" stroke-width="3"/>

      <!-- middle integration ring -->
      <circle r="260" fill="none" stroke="#2a2a2a" stroke-width="162"/>
      <g class="middle-ring" fill="none" stroke-width="160">
        <circle r="260" pathLength="360" stroke="var(--yellow-soft)" stroke-dasharray="87.4 272.6" transform="rotate(-158)"/>
        <circle r="260" pathLength="360" stroke="var(--yellow-deep)" stroke-dasharray="79.4 280.6" transform="rotate(-70)"/>
        <circle r="260" pathLength="360" stroke="var(--olive)" stroke-dasharray="114.4 245.6" transform="rotate(10)"/>
        <circle r="260" pathLength="360" stroke="var(--yellow-mid)" stroke-dasharray="76.4 283.6" transform="rotate(125)"/>
      </g>

      <circle r="180" fill="none" stroke="#8c8c8c" stroke-width="10"/>
      <circle r="175" fill="none" stroke="#3a3a3a" stroke-width="2"/>

      <!-- inner content-management ring -->
      <circle r="174" fill="url(#inner-fill)"/>
      <g class="inner-dividers" stroke="#7a7a7a" stroke-width="3">
        <line x1="0" y1="-174" x2="0" y2="174"/>
        <line x1="-174" y1="0" x2="174" y2="0"/>
      </g>

      <!-- hub -->
      <circle r="78" fill="#8a8a8a"/>
      <circle r="72" fill="url(#hub-fill)"/>
      <text class="brand-mark" x="0" y="20" font-size="58" text-anchor="middle">BD</text>

      <!-- outer labels -->
      <g class="label label-outer">
        <text transform="rotate(-2)"><textPath href="#cw-398" startOffset="50%" text-anchor="middle">Accounting</textPath></text>
        <text transform="rotate(54.5)"><textPath href="#cw-398" startOffset="50%" text-anchor="middle">Project Mgmt</textPath></text>
        <text transform="rotate(-53.5)"><textPath href="#ccw-428" startOffset="50%" text-anchor="middle">Equipment Mgmt</textPath></text>
        <text transform="rotate(1)"><textPath href="#ccw-428" startOffset="50%" text-anchor="middle">HR</textPath></text>
        <text transform="rotate(45.5)"><textPath href="#ccw-428" startOffset="50%" text-anchor="middle">Facilities Mgmt</textPath></text>
        <text transform="rotate(-65.5)"><textPath href="#cw-398" startOffset="50%" text-anchor="middle">Property Mgmt</textPath></text>
      </g>

      <!-- middle labels -->
      <g class="label">
        <text class="label-middle" transform="rotate(-24)"><textPath href="#cw-278" startOffset="50%" text-anchor="middle">NX Office</textPath></text>
        <text class="label-middle" transform="rotate(60)"><textPath href="#cw-262" startOffset="50%" text-anchor="middle">ERP</textPath></text>
        <text class="label-middle" transform="rotate(64)"><textPath href="#ccw-252" startOffset="50%" text-anchor="middle">Sharedeck</textPath></text>
        <text class="label-middle-small" transform="rotate(-28)"><textPath href="#ccw-278" startOffset="50%" text-anchor="middle">Project Mgmt Software</textPath></text>
      </g>

      <!-- inner labels -->
      <g class="label">
        <text class="label-inner" transform="rotate(-42)"><textPath href="#cw-132" startOffset="50%" text-anchor="middle">Capture</textPath></text>
        <text class="label-inner" transform="rotate(40)"><textPath href="#cw-140" startOffset="50%" text-anchor="middle">Document</textPath></text>
        <text class="label-inner-small" transform="rotate(42)"><textPath href="#cw-112" startOffset="50%" text-anchor="middle">Mgmt</textPath></text>
        <text class="label-inner" transform="rotate(44)"><textPath href="#ccw-150" startOffset="50%" text-anchor="middle">Archiving</textPath></text>
        <text class="label-inner" transform="rotate(-42)"><textPath href="#ccw-150" startOffset="50%" text-anchor="middle">Workflow</textPath></text>
      </g>
    </g>

    <!-- small brand badge -->
    <g class="brand-badge" transform="translate(120,910)">
      <circle r="58" fill="#6e6e6e"/>
      <circle r="52" fill="#161616"/>
      <text class="brand-mark" x="0" y="16" font-size="44" text-anchor="middle">BD</text>
    </g>
  </svg>
</div>
</body>
</html>
```